Business Cards for a law firm

Business cards for our law firm. Use our silhoette logo and OAK HARBOR - check our website (www.oakharbor-legal.com)

Contact Information for Business Card

our silhouette logo, OAK HARBOR, 800-555-0147, Dorian Kestrup, dorian@oakharbor-legal.com

Requirements
Must have
• our silhouette logo, OAK HARBOR, 800-555-0147, Dorian Kestrup, dorian@oakharbor-legal.com

```html
<!DOCTYPE html>
<html lang="en">
<head>
<meta charset="utf-8">
<title>Oak Harbor – Business Cards</title>
<link rel="stylesheet" href="https://fonts.googleapis.com/css2?family=Cinzel:wght@600;700&family=Roboto:wght@400&display=swap">
<style>
  :root {
    --page-bg: #1b1c1f;
    --navy-deep: #0d1a45;
    --navy: #13237a;
    --royal: #2b4db0;
    --royal-light: #4f74d2;
    --card-edge: #4a6cc9;
    --ink-light: #ffffff;
  }
  * { box-sizing: border-box; margin: 0; padding: 0; }
  html, body {
    width: 1200px; height: 840px; overflow: hidden;
    background: var(--page-bg);
  }
  .canvas { position: relative; width: 1200px; height: 840px; }

  .card {
    position: absolute;
    width: 640px; height: 366px;
    border-radius: 24px;
    overflow: hidden;
    border: 2px solid var(--card-edge);
    box-shadow: 0 18px 40px rgba(0,0,0,0.55);
  }

  /* Front */
  .card--front { left: 60px; top: 40px; }
  .front-pattern {
    position: absolute; inset: 0;
    background:
      radial-gradient(ellipse at 78% 62%, rgba(79,116,210,0.75) 0%, rgba(43,77,176,0.35) 38%, rgba(19,35,122,0) 70%),
      linear-gradient(115deg, var(--navy-deep) 0%, var(--navy) 45%, var(--royal) 100%);
  }
  .front-brand {
    position: absolute; left: 0; right: 0; top: 50%;
    transform: translateY(-50%);
    display: flex; align-items: center; justify-content: center; gap: 16px;
  }
  .brand-mark {
    width: 22px; height: 22px; border-radius: 50%;
    background: var(--ink-light);
  }
  .brand-name {
    font-family: "Cinzel", serif; font-weight: 700;
    font-size: 44px; letter-spacing: 2px;
    color: var(--ink-light);
  }

  /* Back */
  .card--back { left: 500px; top: 434px; }
  .back-ground {
    position: absolute; inset: 0;
    background: linear-gradient(110deg, var(--navy-deep) 0%, var(--navy) 55%, #1a3590 100%);
  }
  .emblem-area {
    position: absolute; right: 0; top: 0; bottom: 0; width: 40%;
    background: linear-gradient(160deg, rgba(255,255,255,0.85) 0%, rgba(220,228,250,0.75) 55%, rgba(79,116,210,0.35) 100%);
  }
  .back-brand {
    position: absolute; left: 40px; top: 62px;
    font-family: "Cinzel", serif; font-weight: 700;
    font-size: 34px; letter-spacing: 1.5px;
    color: var(--ink-light);
    white-space: nowrap;
  }
  .contact-block {
    position: absolute; left: 56px; bottom: 40px;
    color: var(--ink-light);
  }
  .contact-name {
    font-family: "Cinzel", serif; font-weight: 700;
    font-size: 22px; letter-spacing: 1.5px;
    margin-bottom: 10px;
    white-space: nowrap;
  }
  .contact-list { list-style: none; }
  .contact-item {
    display: flex; align-items: center; gap: 10px;
    font-family: "Roboto", sans-serif; font-size: 17px;
    line-height: 30px;
    white-space: nowrap;
  }
  .contact-icon { width: 16px; height: 16px; flex: none; }
</style>
</head>
<body>
<main class="canvas">

  <section class="card card--front" aria-label="Card front">
    <div class="front-pattern" role="img" aria-label="Repeating pattern of paired-figure silhouettes in shades of blue"></div>
    <div class="front-brand">
      <span class="brand-mark"></span>
      <span class="brand-name">OAK HARBOR</span>
    </div>
  </section>

  <section class="card card--back" aria-label="Card back">
    <div class="back-ground"></div>
    <div class="emblem-area" role="img" aria-label="Large white silhouette emblem of two standing figures"></div>
    <h1 class="back-brand">OAK HARBOR</h1>
    <div class="contact-block">
      <p class="contact-name">DORIAN KESTRUP</p>
      <ul class="contact-list">
        <li class="contact-item">
          <svg class="contact-icon" viewBox="0 0 24 24" aria-hidden="true">
            <path fill="#fff" d="M6.6 10.8a15.1 15.1 0 0 0 6.6 6.6l2.2-2.2a1 1 0 0 1 1-.25 11.4 11.4 0 0 0 3.6.57 1 1 0 0 1 1 1V20a1 1 0 0 1-1 1A17 17 0 0 1 3 4a1 1 0 0 1 1-1h3.5a1 1 0 0 1 1 1c0 1.25.2 2.45.57 3.570a1 1 0 0 1-.25 1z"/>
          </svg>
          <span>800-555-0147</span>
        </li>
        <li class="contact-item">
          <svg class="contact-icon" viewBox="0 0 24 24" aria-hidden="true">
            <rect x="2" y="5" width="20" height="14" rx="1.5" fill="#fff"/>
            <path d="M3 6.5l9 6.5 9-6.5" fill="none" stroke="#13237a" stroke-width="1.8"/>
          </svg>
          <span>dorian@oakharbor-legal.com</span>
        </li>
        <li class="contact-item">
          <svg class="contact-icon" viewBox="0 0 24 24" aria-hidden="true">
            <circle cx="12" cy="12" r="10" fill="#fff"/>
            <g fill="none" stroke="#13237a" stroke-width="1.5">
              <ellipse cx="12" cy="12" rx="4.5" ry="10"/>
              <path d="M2 12h20M4 7h16M4 17h16"/>
            </g>
          </svg>
          <span>www.oakharbor-legal.com</span>
        </li>
      </ul>
    </div>
  </section>

</main>
</body>
</html>
```